LITTLE DESIGN WORK REQUIRED!

UPDATE: WE WEREN'T OVERLY ECSTATIC WITH THE DESIGNS WE WERE RECEIVING SO WE DID MOST OF THE DESIGN WORK OURSELVES...

PLEASE SEE THE NEWLY ATTACHED PPT DOC TO VIEW NEARLY EXACT REPLICAS OF WHAT WE WANT THE SITE TO LOOK LIKE. WE NOW NEED YOUR HELP TO MAKE IT LOOK LIKE SOMETHING WORTHY OF THE WEB.

NO CODING REQUIRED - EXPECTED OUTPUT PSD FILES

Hi everyone!

We're looking for a designer to work their magic for our site! We're a not-for-profit program aimed at helping young people realise their potential!

In the attached PPT file, you'll notice we've already DESIGNED THE ENTIRE SITE IN POWERPOINT. Now, we need YOU to make the small changes we requested in the document as well as design the whole thing in psd.

Any questions, don't hesitate to ask.

Brook-Rise
Updates

We've done about 95% of the design for you. Please fine-tune it. See the newly attached PPT doc for details. 

The best two designs will win. This project closes on Friday - please message us if you are absolutely sure you cannot make the deadline.

Thanks,
Brook-Rise

```html
<!DOCTYPE html>
<html lang="en">
<head>
<meta charset="utf-8">
<title>Brook-Rise</title>
<link rel="stylesheet" href="https://fonts.googleapis.com/css2?family=Open+Sans:ital,wght@0,400;0,600;0,700;1,400;1,600&family=PT+Sans:ital,wght@0,400;0,700;1,400;1,700&display=swap">
<style>
:root{
  --bg-outer:#b9b9b7;
  --bg-column:#f6f6f6;
  --ink:#1f1f1f;
  --ink-soft:#555;
  --ink-muted:#8a8a8a;
  --green:#5aa51b;
  --green-light:#7cc42a;
  --green-dark:#2f6e0e;
  --navy:#2c4a80;
  --orange:#e07a18;
  --red:#c8141c;
  --bright-green:#23ad23;
  --footer-top:#3a3a3a;
  --footer-bottom:#151515;
  --white:#fff;
}
*{box-sizing:border-box;margin:0;padding:0}
html,body{width:1200px;height:2531px;overflow:hidden}
body{background:var(--bg-outer);font-family:"Open Sans",Arial,sans-serif;color:var(--ink)}
.page{position:relative;width:1200px;height:2531px;overflow:hidden;
  background:linear-gradient(90deg,#a9a9a7,#c4c4c2 6%,#c4c4c2 94%,#a9a9a7)}
.abs{position:absolute}
.column{left:74px;top:0;width:1054px;height:2215px;background:var(--bg-column);
  box-shadow:0 0 14px rgba(0,0,0,.25)}

/* header */
.brand{left:169px;top:40px;display:flex;align-items:center;gap:16px}
.brand-mark{width:46px;height:46px;border-radius:50%;background:var(--green)}
.brand-name{font-family:"PT Sans",sans-serif;font-weight:700;font-size:58px;color:#111;letter-spacing:-1px}
.quote{left:625px;top:30px;width:440px;text-align:center;font-family:"PT Sans",sans-serif;
  font-style:italic;color:var(--ink-muted);font-size:30px;line-height:32px}
.quote-author{left:690px;top:96px;font-family:"PT Sans",sans-serif;color:var(--ink-muted);font-size:27px}
.share-btn{left:907px;top:98px;width:86px;height:30px;background:#5872a8;border:1px solid #3b5488;
  border-radius:3px;color:#fff;font-size:14px;font-weight:700;display:flex;align-items:center;gap:6px;padding-left:6px}
.share-btn i{width:18px;height:18px;background:#fff;border-radius:2px;display:block}

/* nav */
.nav{left:162px;top:173px;height:70px}
.nav a{position:absolute;top:0;height:70px;border-radius:9px;background:linear-gradient(#3d3d3d,#1c1c1c);
  color:#fff;text-decoration:none;font-size:27px;display:flex;align-items:center;justify-content:center;
  box-shadow:0 2px 3px rgba(0,0,0,.3)}
.nav a.active{background:linear-gradient(var(--green-light),#3f8e12)}

/* hero */
.hero-photo{left:162px;top:268px;width:574px;height:302px;
  background:linear-gradient(#4a6ec4 0%,#8aa8d8 30%,#5a5a7a 48%,#4f7a2c 62%,#6e9a30 100%)}
.feats{left:747px;top:268px;width:287px;height:302px;background:linear-gradient(#7cc42a,#3c8a10);
  color:#fff;text-align:center}
.feats-title{margin:52px auto 0;width:200px;border-top:4px solid #fff;border-bottom:4px solid #fff;
  font-family:"PT Sans",sans-serif;font-weight:700;font-size:68px;line-height:78px}
.feats-text{margin-top:40px;font-size:27px;line-height:32px}
.dots{left:166px;top:584px;display:flex;gap:7px}
.dots span{width:25px;height:25px;border-radius:50%;background:var(--green);border:2px solid #cfe8b3}

/* welcome */
.welcome-title{left:154px;top:610px;font-family:"PT Sans",sans-serif;font-style:italic;font-size:50px;line-height:58px;color:var(--green-dark)}
.welcome-title em{color:var(--green-light)}
.welcome-text{left:154px;top:672px;width:560px;font-family:"PT Sans",sans-serif;font-size:25px;line-height:25px;color:var(--ink-soft)}
.read-more{left:154px;top:774px;font-size:18px;line-height:22px;font-weight:700;color:#222}

/* recent posts */
.posts-panel{left:137px;top:816px;width:570px;height:1372px;background:#fff;
  box-shadow:0 2px 10px rgba(0,0,0,.3)}
.posts-title{left:163px;top:822px;font-family:"PT Sans",sans-serif;font-size:46px;color:#111}
.pin{left:650px;top:832px;width:40px;height:40px;border-radius:50%;
  background:radial-gradient(circle at 35% 35%,#ff6b6b,#c00 60%,#800)}
.cat{position:absolute;left:162px;width:526px;height:300px}
.cat-bar{height:27px;color:#fff;font-style:italic;font-size:24px;line-height:27px;padding-left:12px;
  display:flex;justify-content:space-between;padding-right:12px}
.cat-bar b{font-style:normal}
.cat.discover .cat-bar{background:linear-gradient(90deg,var(--navy),#3a5c98)}
.cat.design .cat-bar{background:linear-gradient(90deg,var(--orange),#c8600c)}
.cat.build .cat-bar{background:linear-gradient(90deg,var(--red),#a40c12)}
.cat.achieve .cat-bar{background:linear-gradient(90deg,var(--bright-green),#14951a)}
.post{position:absolute;top:51px;width:250px;height:260px}
.post.left{left:11px}.post.right{left:292px}
.post-photo{width:219px;height:148px;box-shadow:0 3px 7px rgba(0,0,0,.35)}
.post-title{margin-top:12px;font-weight:700;font-size:20px;line-height:24px;color:#111;white-space:nowrap}
.post-text{margin-top:2px;width:245px;font-size:14px;line-height:18px;color:#666}
.share-row{position:absolute;top:232px;left:95px;display:flex;gap:4px;align-items:center}
.mini{height:20px;padding:0 5px;border:1px solid #bbb;border-radius:3px;background:#f2f2f2;
  font-size:11px;color:#335;line-height:18px}
.count{width:26px;height:22px;border-radius:3px;background:#666;color:#fff;font-size:13px;text-align:center;line-height:22px}

/* sidebar */
.side-head{font-family:"PT Sans",sans-serif;font-size:46px;text-align:center;width:300px}
.stay{left:766px;top:608px;color:var(--navy)}
.like-box{left:791px;top:675px;width:249px;height:47px;background:#fff;border:1px solid #9aa6c0;
  display:flex;align-items:center;gap:8px;padding:0 6px;font-size:13px;line-height:15px;color:#333}
.like-box .mini{flex:none}
.activity{left:785px;top:738px;width:255px;height:285px;background:#fff;border:1px solid #9aa6c0;
  font-size:11px;color:#333}
.activity-head{height:24px;background:#3b5998;color:#fff;font-size:12px;display:flex;justify-content:space-between;
  align-items:center;padding:0 8px}
.activity-item{display:flex;gap:6px;padding:6px 8px 0}
.activity-item i{flex:none;width:28px;height:28px;background:#6d84b4}
.activity-item b{color:#3b5998;display:block;font-size:11px;line-height:13px}
.activity-item span{color:#888;font-size:9px}
.activity-foot{position:absolute;bottom:0;left:0;right:0;height:18px;border-top:1px solid #ddd;
  font-size:9px;color:#888;padding-left:8px;line-height:17px}
.popular{left:766px;top:1034px;color:var(--green)}
.pop-box{left:785px;top:1088px;width:316px;height:330px;border-radius:10px;
  background:linear-gradient(#eef3e6,#dfe6d6);box-shadow:0 2px 6px rgba(0,0,0,.3);padding:12px 18px}
.pop-item{display:flex;justify-content:space-between;align-items:flex-end;height:61px;
  border-bottom:2px solid #666;font-size:21px;line-height:22px;color:#223;padding-bottom:4px}
.pop-item:last-child{border-bottom:0}
.pop-item small{font-size:15px;color:#444}
.know{left:746px;top:1452px;width:340px;color:#333}
.person{position:absolute;left:810px;width:300px}
.person-photo{width:211px;height:211px}
.person-name{margin-top:8px;font-weight:700;font-size:23px;color:#111}
.person-role{font-style:italic;font-size:19px;line-height:23px;color:#222}
.person-link{margin-top:4px;font-size:17px;color:#222}

/* footer */
.footer{left:0;top:2215px;width:1200px;height:274px;background:linear-gradient(var(--footer-top),var(--footer-bottom))}
.search{left:74px;top:2262px;width:295px;height:51px;background:#fff;border-radius:6px;
  box-shadow:0 0 6px rgba(255,255,255,.4)}
.search-btn{left:281px;top:2268px;width:84px;height:39px;background:linear-gradient(var(--green-light),#3f8e12);
  color:#fff;font-size:17px;font-weight:700;display:flex;align-items:center;justify-content:center}
.foot-brand{left:42px;top:2372px;display:flex;align-items:center;gap:14px}
.foot-brand .brand-name{color:#0c0c0c;font-size:56px}
.foot-brand .brand-mark{width:42px;height:42px}
.vline{width:2px;background:#666}
.foot-links{left:405px;top:2254px;font-size:19px;line-height:17px;color:#eee;list-style:none}
.follow{left:584px;top:2254px;font-size:19px;line-height:22px;color:#eee}
.social{top:2284px;width:46px;height:46px;border-radius:6px}
.contact{left:730px;top:2258px;width:426px;height:173px;border:2px solid #555;padding:8px 8px}
.contact h3{font-weight:400;font-size:23px;color:#eee}
.field{position:absolute;left:38px;font-size:19px;line-height:24px;color:#eee}
.input{position:absolute;left:184px;width:186px;background:#777;border:1px solid #888}
.bottom-bar{left:0;top:2489px;width:1200px;height:42px;background:linear-gradient(var(--green-light),#3f8e12);
  color:#fff;font-size:17px;text-align:right;padding-right:34px;line-height:42px}
</style>
</head>
<body>
<div class="page">
  <div class="abs column"></div>

  <header>
    <div class="abs brand"><span class="brand-mark"></span><span class="brand-name">Brook-Rise</span></div>
    <p class="abs quote">“What would you do if you knew you could not fail?”</p>
    <p class="abs quote-author">- R. Hollin</p>
    <div class="abs share-btn"><i></i>SHARE</div>
  </header>

  <nav class="abs nav">
    <a class="active" style="left:0;width:93px">Home</a>
    <a style="left:102px;width:141px">About us</a>
    <a style="left:251px;width:152px">Resources</a>
    <a style="left:412px;width:160px">Workshops</a>
    <a style="left:581px;width:189px">Ambassadors</a>
    <a style="left:779px;width:95px">Feats</a>
  </nav>

  <div class="abs hero-photo" role="img" aria-label="Photo of elephants walking across green grassland beneath a snow-capped mountain"></div>
  <div class="abs feats">
    <div class="feats-title">FEATS</div>
    <p class="feats-text">Challenges that<br>dare you to<br>push yourself.</p>
  </div>
  <div class="abs dots"><span></span><span></span><span></span><span></span></div>

  <h1 class="abs welcome-title">Welcome to <em>Brook-Rise</em></h1>
  <p class="abs welcome-text">Brook-Rise is a not-for-profit program aimed at helping people – especially young people – set and achieve authentic, meaningful, and audacious goals.</p>
  <p class="abs read-more">&gt;read more</p>

  <div class="abs posts-panel"></div>
  <h2 class="abs posts-title">Recent Posts</h2>
  <div class="abs pin"></div>

  <section class="cat discover" style="top:897px">
    <div class="cat-bar">Discover<b>?</b></div>
    <article class="post left">
      <div class="post-photo" role="img" aria-label="Photo of students studying together on a lawn" style="background:linear-gradient(#6d8a3a,#c8c0a8)"></div>
      <h3 class="post-title">Title A Lorem Ipsum</h3>
      <p class="post-text">Clarity about who you are, what<br>you want, and why you want it.</p>
      <div class="share-row"><span class="mini">Tweet</span><span class="mini">Like</span><span class="count">5</span></div>
    </article>
    <article class="post right">
      <div class="post-photo" role="img" aria-label="Photo of a silhouetted figure with arms raised against a blue sky" style="background:linear-gradient(#1e4fa8,#8ab4e8)"></div>
      <h3 class="post-title">Title B Lorem Ipsum</h3>
      <p class="post-text">Lorem ipsum dosectetur<br>adipisicing elit, sed do.</p>
      <div class="share-row"><span class="mini">Tweet</span><span class="mini">Like</span><span class="count">5</span></div>
    </article>
  </section>

  <section class="cat design" style="top:1222px">
    <div class="cat-bar">Design<b>?</b></div>
    <article class="post left">
      <div class="post-photo" role="img" aria-label="Photo of a person in a suit turning pages of a notebook" style="background:linear-gradient(#2a2a2a,#bdbdbd)"></div>
      <h3 class="post-title">Title C Lorem Ipsum</h3>
      <p class="post-text">Clarity about who you are, what<br>you want, and why you want it.</p>
      <div class="share-row"><span class="mini">Tweet</span><span class="mini">Like</span><span class="count">5</span></div>
    </article>
    <article class="post right">
      <div class="post-photo" role="img" aria-label="Photo of a sprinter running on a track" style="background:linear-gradient(90deg,#c8b020,#5a8a20,#d8c860)"></div>
      <h3 class="post-title">Title D Lorem Ipsum</h3>
      <p class="post-text">Lorem ipsum dosectetur<br>adipisicing elit, sed do.</p>
      <div class="share-row"><span class="mini">Tweet</span><span class="mini">Like</span><span class="count">5</span></div>
    </article>
  </section>

  <section class="cat build" style="top:1547px">
    <div class="cat-bar">Build<b>?</b></div>
    <article class="post left">
      <div class="post-photo" role="img" aria-label="Photo of a business team in a bright office" style="background:linear-gradient(#e8edf2,#8d96a3)"></div>
      <h3 class="post-title">Title E Lorem Ipsum</h3>
      <p class="post-text">Clarity about who you are, what<br>you want, and why you want it.</p>
      <div class="share-row"><span class="mini">Tweet</span><span class="mini">Like</span><span class="count">5</span></div>
    </article>
    <article class="post right">
      <div class="post-photo" role="img" aria-label="Photo of a child blowing a dandelion in a green field" style="background:linear-gradient(#8cc04a,#3e7a1a)"></div>
      <h3 class="post-title">Title F Lorem Ipsum</h3>
      <p class="post-text">Lorem ipsum dosectetur<br>adipisicing elit, sed do.</p>
      <div class="share-row"><span class="mini">Tweet</span><span class="mini">Like</span><span class="count">5</span></div>
    </article>
  </section>

  <section class="cat achieve" style="top:1872px">
    <div class="cat-bar">Achieve<b>?</b></div>
    <article class="post left">
      <div class="post-photo" role="img" aria-label="Photo of a business team in a bright office" style="background:linear-gradient(#e8edf2,#8d96a3)"></div>
      <h3 class="post-title">Title G Lorem Ipsum</h3>
      <p class="post-text">Clarity about who you are, what<br>you want, and why you want it.</p>
      <div class="share-row"><span class="mini">Tweet</span><span class="mini">Like</span><span class="count">5</span></div>
    </article>
    <article class="post right">
      <div class="post-photo" role="img" aria-label="Photo of a child blowing a dandelion in a green field" style="background:linear-gradient(#8cc04a,#3e7a1a)"></div>
      <h3 class="post-title">Title H Lorem Ipsum</h3>
      <p class="post-text">Lorem ipsum dosectetur<br>adipisicing elit, sed do.</p>
      <div class="share-row"><span class="mini">Tweet</span><span class="mini">Like</span><span class="count">5</span></div>
    </article>
  </section>

  <aside>
    <h2 class="abs side-head stay">Stay In Touch</h2>
    <div class="abs like-box"><span class="mini">Like</span><span>22 people like this. Be the first of your friends.</span></div>
    <div class="abs activity">
      <div class="activity-head"><span>Recent Activity</span><b>Circlebook</b></div>
      <div class="activity-item"><i></i><div><b>Join the Spring Founders Circle Today</b><span>1,891 people shared this.</span></div></div>
      <div class="activity-item"><i></i><div><b>Platform Notes: New Tools and Guides</b><span>1,866 people shared this.</span></div></div>
      <div class="activity-item"><i></i><div><b>Planning Roles and Team Safety</b><span>1,260 people shared this.</span></div></div>
      <div class="activity-item"><i></i><div><b>Next Step for Youth Grants</b><span>3,363 people shared this.</span></div></div>
      <div class="activity-item"><i></i><div><b>Web Skills Night 0.1</b><span>752 people shared this.</span></div></div>
      <div class="activity-foot">Social plugin</div>
    </div>

    <h2 class="abs side-head popular">Popular Posts</h2>
    <ol class="abs pop-box" style="list-style:none">
      <li class="pop-item"><span>1. Lorem ipsum<br>dosectetur.</span><small>587 view(s)</small></li>
      <li class="pop-item"><span>2. Lorem ipsum<br>dosectetur.</span><small>587 view(s)</small></li>
      <li class="pop-item"><span>3. Lorem ipsum<br>dosectetur.</span><small>587 view(s)</small></li>
      <li class="pop-item"><span>4. Lorem ipsum<br>dosectetur.</span><small>587 view(s)</small></li>
      <li class="pop-item"><span>5. Lorem ipsum<br>dosectetur.</span><small>587 view(s)</small></li>
    </ol>

    <h2 class="abs side-head know">Get To Know Us</h2>
    <div class="person" style="top:1511px">
      <div class="person-photo" role="img" aria-label="Portrait photo of ambassador John Doe" style="background:linear-gradient(#2a5ab8,#0e2a6a)"></div>
      <p class="person-name">John Doe</p>
      <p class="person-role">Young entrepreneur<br>&amp; Brook-Rise Ambassador</p>
      <p class="person-link">&gt;meet John</p>
    </div>
    <div class="person" style="top:1836px">
      <div class="person-photo" role="img" aria-label="Photo of ambassador Jane Smith playing tennis" style="background:linear-gradient(#4a88d8,#d86a80 70%,#b8a0a8)"></div>
      <p class="person-name">Jane Smith</p>
      <p class="person-role">Professional athlete<br>&amp; Brook-Rise Ambassador</p>
      <p class="person-link">&gt;meet Jane</p>
    </div>
  </aside>

  <footer>
    <div class="abs footer"></div>
    <div class="abs search"></div>
    <div class="abs search-btn">SEARCH</div>
    <div class="abs foot-brand"><span class="brand-mark"></span><span class="brand-name">Brook-Rise</span></div>
    <div class="abs vline" style="left:397px;top:2254px;height:206px"></div>
    <ul class="abs foot-links">
      <li>Home</li><li>About us</li><li>Resources</li><li>Workshops</li><li>Ambassadors</li><li>Feats</li>
    </ul>
    <div class="abs vline" style="left:576px;top:2254px;height:206px"></div>
    <p class="abs follow">Follow us on:</p>
    <div class="abs social" style="left:584px;background:#3b64b0"></div>
    <div class="abs social" style="left:633px;background:#3fb4e8"></div>
    <div class="abs contact">
      <h3>Contact Us:</h3>
      <span class="field" style="top:44px">Name</span>
      <span class="field" style="top:70px">Email</span>
      <span class="field" style="top:96px">Message</span>
      <span class="input" style="top:46px;height:24px"></span>
      <span class="input" style="top:72px;height:24px"></span>
      <span class="input" style="top:98px;height:62px"></span>
    </div>
    <div class="abs bottom-bar">© 2012 Brook-Rise&nbsp; All Rights Reserved</div>
  </footer>
</div>
</body>
</html>
```